Premium Epoxy Distributor Needs Landing Page Design and Copy Writing

We need a high converting landing page with full service design and copy writing for our search engine marketing campaign. We are the exclusive distributor for a US manufacturer of high quality, industrial grade garage floor epoxies. Our primarily market is the DIY (do-it-yourself) within the US. Our unique selling proposition is that we are able to provide industrial grade epoxies to the public which were only available to contractors and professional installers before.

The final design should be modern, sleek and visually appealing. The copy writing should be clear and succinct, and communicate the benefits of our product and tailored for the DIY market.

We have not chosen a land page platform, but were looking at Shogun or Unbounce.

Target Market(s)

Garage Floor Epoxy market with a concentrated focus on the DIYer (Do It Yourself).
Home improvement market.

Requirements
Must have
• Excellent copy writing, someone who is familiar with the home improvement market, garage floor epoxies or the coatings industry is a plus.
Nice to have
• We have invested heavily into a custom product configurator which provides real time pricing for each individual project based on square footage. If you think this is something of value please add it to the landing page content.

```html
<!DOCTYPE html>
<html lang="en">
<head>
<meta charset="utf-8">
<title>Ridgeline Coatings – Industrial Garage Floor Epoxy for DIY</title>
<link href="https://fonts.googleapis.com/css2?family=Roboto:ital,wght@0,400;0,500;0,700;1,400&display=swap" rel="stylesheet">
<style>
:root{
  --canvas:#e7e7e7;
  --white:#ffffff;
  --red:#e0141f;
  --ink:#2b2b2b;
  --muted:#666666;
  --dark:#39393b;
  --gold:#f2b705;
}
*{margin:0;padding:0;box-sizing:border-box}
html,body{width:879px;height:1200px;overflow:hidden;background:var(--canvas);font-family:'Roboto',Arial,sans-serif;color:var(--ink)}
.page{position:absolute;top:57px;width:377px;height:1074px;background:var(--white);overflow:hidden;box-shadow:0 0 4px rgba(0,0,0,.08)}
.page--a{left:43px}
.page--b{left:459px}
.abs{position:absolute}
.red{color:var(--red)}

.hero{left:0;top:0;width:377px;height:191px;
  background:
    linear-gradient(160deg,rgba(214,140,40,0) 55%,rgba(214,140,40,.35) 75%,rgba(214,140,40,0) 90%),
    linear-gradient(180deg,#9a978f 0%,#8a8780 30%,#6e7173 52%,#5b5f62 75%,#45484a 100%)}
.hero-shade{left:0;top:0;width:377px;height:191px;background:rgba(0,0,0,.22)}
.brand{position:absolute;display:flex;align-items:center;gap:3px;font-weight:700;font-size:8px;letter-spacing:.3px;color:var(--white);white-space:nowrap}
.brand-dot{width:8px;height:8px;border-radius:50%;background:var(--red)}
.hero-title{left:0;width:377px;text-align:center;font-weight:500;font-size:12.5px;color:var(--white)}
.hero-text{left:0;width:377px;text-align:center;font-size:5.2px;line-height:8.5px;color:var(--white);font-weight:500}
.btn{position:absolute;height:13px;border-radius:7px;background:var(--red);color:var(--white);font-size:5.2px;font-weight:700;display:flex;align-items:center;justify-content:center;white-space:nowrap}

.section-title{left:0;width:377px;text-align:center;font-weight:500;font-size:12.5px;color:var(--ink)}
.benefit{width:96px;text-align:center}
.benefit-icon{display:block;margin:0 auto 6px;width:16px;height:16px}
.benefit-name{font-size:5.2px;font-weight:700;color:var(--ink);margin-bottom:6px}
.benefit-text{font-size:4.5px;line-height:7px;color:var(--muted)}

.how{left:0;top:339px;width:377px;height:149px;background:var(--dark)}
.how-text{left:0;width:377px;text-align:center;font-size:4.5px;line-height:7.5px;color:#e2e2e2}
.video{left:37px;top:410px;width:303px;height:150px;
  background:linear-gradient(180deg,#6fa3d6 0%,#a9c5e0 35%,#8a9aa0 50%,#6d7d72 62%,#8f8a6a 78%,#c98d3c 100%)}
.play{left:176px;top:473px;width:24px;height:24px}

.review{width:144px}
.stars{font-size:4.5px;color:var(--gold);letter-spacing:.5px}
.review-text{margin-top:4px;font-size:4.5px;line-height:7px;font-style:italic;color:var(--muted)}
.reviewer{margin-top:9px;display:flex;align-items:center;gap:4px}
.avatar{width:18px;height:18px;border-radius:50%;background:linear-gradient(135deg,#8a786a,#2d2a28)}
.reviewer-name{font-size:5px;font-weight:500;color:var(--ink)}
.reviewer-role{font-size:3.5px;color:var(--muted);margin-top:2px}

.card{width:96px}
.card-photo{width:96px;height:53px}
.card-photo--lift{background:linear-gradient(180deg,#c3cad4 0%,#2c4ea6 40%,#3a5cb0 60%,#b7c3d2 100%)}
.card-photo--lounge{background:linear-gradient(180deg,#eeeeec 0%,#cfccc6 55%,#8d857e 100%)}
.card-photo--hall{background:linear-gradient(180deg,#3f4146 0%,#8e949b 40%,#cfd3d8 70%,#a4a9ae 100%)}
.card-title{margin-top:8px;font-size:5px;font-weight:500;color:var(--ink)}
.card-text{margin-top:5px;font-size:4.5px;line-height:7.5px;color:var(--muted)}

.about-photo{left:35px;top:865px;width:150px;height:128px;background:linear-gradient(180deg,#aab0b7 0%,#c9ced3 30%,#6f7b8c 45%,#dcdfe2 60%,#a9b0b5 100%)}
.about-label{left:217px;top:895px;font-size:5px;font-weight:700;color:var(--red)}
.about-title{left:217px;top:903px;font-size:12.5px;font-weight:500;color:var(--ink);white-space:nowrap}
.about-text{left:217px;top:924px;width:126px;font-size:4.5px;line-height:8px;color:var(--muted)}

.footer{left:0;top:1016px;width:377px;height:58px;background:var(--dark)}
.copyright{right:35px;top:20px;font-size:4.3px;color:#dcdcdc}
</style>
</head>
<body>

<!-- Version A: call to action under the headline -->
<section class="page page--a">
  <div class="abs hero" role="img" aria-label="Glossy epoxy-coated warehouse floor with orange lane markings and tall loading doors"></div>
  <div class="abs hero-shade"></div>
  <div class="brand" style="left:116px;top:24px"><span class="brand-dot"></span>RIDGELINE COATINGS</div>
  <h1 class="abs hero-title" style="top:77px">EPOXY <span class="red">DISTRIBUTOR</span></h1>
  <p class="abs hero-text" style="top:96px">Industrial-grade garage floor epoxy, once sold only to contractors,<br>now shipped straight to your door for a pro finish you install yourself.</p>
  <a class="btn" style="left:135px;top:121px;width:108px">Create your custom garage floor now</a>

  <h2 class="abs section-title" style="top:221px">OUR <span class="red">BENEFITS</span></h2>
  <div class="abs benefit" style="left:43px;top:252px">
    <svg class="benefit-icon" viewBox="0 0 16 16" fill="none" stroke="#555" stroke-width=".8"><rect x="3" y="1" width="10" height="10"/><line x1="5" y1="4" x2="11" y2="4"/><line x1="5" y1="6" x2="11" y2="6"/><circle cx="8" cy="13" r="2.5" stroke="#e0141f"/></svg>
    <div class="benefit-name">Contractor-grade strength</div>
    <div class="benefit-text">The same industrial epoxy the pros use, built to resist hot tires, oil and chemicals.</div>
  </div>
  <div class="abs benefit" style="left:146px;top:252px">
    <svg class="benefit-icon" viewBox="0 0 16 16" fill="none" stroke="#555" stroke-width=".8"><circle cx="8" cy="5" r="3.5" stroke="#e0141f"/><path d="M1 9l3 4h3M15 9l-3 4H9"/></svg>
    <div class="benefit-name">Save thousands doing it yourself</div>
    <div class="benefit-text">Skip installer markups and pay only for the product your floor actually needs.</div>
  </div>
  <div class="abs benefit" style="left:248px;top:252px">
    <svg class="benefit-icon" viewBox="0 0 16 16" fill="none" stroke="#555" stroke-width=".8"><circle cx="8" cy="5" r="3.5" stroke="#e0141f"/><path d="M8 3v2h1.5" stroke="#e0141f"/><path d="M1 9l3 4h3M15 9l-3 4H9"/></svg>
    <div class="benefit-name">Finished in one weekend</div>
    <div class="benefit-text">Complete kits with clear step-by-step guides, so you can park on it by Monday.</div>
  </div>

  <div class="abs how"></div>
  <h2 class="abs section-title" style="top:359px;color:var(--white)">HOW IT WORKS</h2>
  <p class="abs how-text" style="top:378px">Pick your coating and colour, enter your garage's square footage and our configurator shows your exact price in real time.<br>We ship a complete kit with everything you need, from floor prep to topcoat, right to your driveway.</p>
  <div class="abs video" role="img" aria-label="Video still of an industrial coatings plant at sunset"></div>
  <svg class="abs play" viewBox="0 0 24 24"><circle cx="12" cy="12" r="12" fill="#e0141f"/><path d="M9.5 7.5v9l7-4.5z" fill="#fff"/></svg>

  <h2 class="abs section-title" style="top:592px">CLIENT <span class="red">REVIEWS</span></h2>
  <div class="abs review" style="left:35px;top:629px">
    <div class="stars">★★★★★</div>
    <p class="review-text">I was quoted over four thousand dollars by a local installer. I did the whole two-car garage myself in a weekend for a fraction of that, and it still looks like a showroom floor a year later.</p>
    <div class="reviewer"><div class="avatar" role="img" aria-label="Reviewer portrait"></div><div><div class="reviewer-name">John Doe</div><div class="reviewer-role">UAS</div></div></div>
  </div>
  <div class="abs review" style="left:197px;top:629px">
    <div class="stars">★★★★★</div>
    <p class="review-text">The configurator gave me an exact price before I ordered, and the kit had everything down to the rollers. Hot tires, oil drips and dropped tools haven't left a single mark on it.</p>
    <div class="reviewer"><div class="avatar" role="img" aria-label="Reviewer portrait"></div><div><div class="reviewer-name">John Doe</div><div class="reviewer-role">UAS</div></div></div>
  </div>

  <div class="abs card" style="left:37px;top:725px">
    <div class="card-photo card-photo--lift" role="img" aria-label="Workshop with blue car lifts on a glossy epoxy floor"></div>
    <div class="card-title">METALLIC EPOXY COATING</div>
    <p class="card-text">A deep, glossy metallic finish that stands up to car lifts, jacks and heavy tool chests.</p>
  </div>
  <div class="abs card" style="left:140px;top:725px">
    <div class="card-photo card-photo--lounge" role="img" aria-label="Bright living room with a polished epoxy floor"></div>
    <div class="card-title">METALLIC EPOXY COATING</div>
    <p class="card-text">Seamless and easy to clean, perfect for basements, home gyms and living spaces.</p>
  </div>
  <div class="abs card" style="left:243px;top:725px">
    <div class="card-photo card-photo--hall" role="img" aria-label="Long glossy corridor floor in a parking garage"></div>
    <div class="card-title">METALLIC EPOXY COATING</div>
    <p class="card-text">Chemical and abrasion resistant for high-traffic garages, shops and driveways.</p>
  </div>

  <div class="abs about-photo" role="img" aria-label="Large empty warehouse with a reflective epoxy floor"></div>
  <div class="abs about-label">ABOUT</div>
  <h2 class="abs about-title">RIDGELINE <span class="red">COATINGS</span></h2>
  <p class="abs about-text">We are the exclusive distributor of a US manufacturer of industrial-grade floor epoxies. For years these coatings were sold only to contractors and professional installers. Now we bring that same quality directly to homeowners, with kits, guides and real-time pricing made for DIY.</p>

  <footer class="abs footer">
    <div class="brand" style="left:35px;top:25px"><span class="brand-dot"></span>RIDGELINE COATINGS</div>
    <p class="abs copyright">© Copyright 2020 Ridgeline Coatings. All Rights Reserved</p>
  </footer>
</section>

<!-- Version B: call to action in the header -->
<section class="page page--b">
  <div class="abs hero" role="img" aria-label="Glossy epoxy-coated warehouse floor with orange lane markings and tall loading doors"></div>
  <div class="abs hero-shade"></div>
  <div class="brand" style="left:36px;top:24px"><span class="brand-dot"></span>RIDGELINE COATINGS</div>
  <a class="btn" style="left:234px;top:19px;width:107px">Create your custom garage floor now</a>
  <h1 class="abs hero-title" style="top:84px">EPOXY <span class="red">DISTRIBUTOR</span></h1>
  <p class="abs hero-text" style="top:104px">Industrial-grade garage floor epoxy, once sold only to contractors, now shipped<br>straight to your door for a pro finish you install yourself.</p>

  <h2 class="abs section-title" style="top:221px">OUR <span class="red">BENEFITS</span></h2>
  <div class="abs benefit" style="left:43px;top:252px">
    <svg class="benefit-icon" viewBox="0 0 16 16" fill="none" stroke="#555" stroke-width=".8"><rect x="3" y="1" width="10" height="10"/><line x1="5" y1="4" x2="11" y2="4"/><line x1="5" y1="6" x2="11" y2="6"/><circle cx="8" cy="13" r="2.5" stroke="#e0141f"/></svg>
    <div class="benefit-name">Contractor-grade strength</div>
    <div class="benefit-text">The same industrial epoxy the pros use, built to resist hot tires, oil and chemicals.</div>
  </div>
  <div class="abs benefit" style="left:146px;top:252px">
    <svg class="benefit-icon" viewBox="0 0 16 16" fill="none" stroke="#555" stroke-width=".8"><circle cx="8" cy="5" r="3.5" stroke="#e0141f"/><path d="M1 9l3 4h3M15 9l-3 4H9"/></svg>
    <div class="benefit-name">Save thousands doing it yourself</div>
    <div class="benefit-text">Skip installer markups and pay only for the product your floor actually needs.</div>
  </div>
  <div class="abs benefit" style="left:248px;top:252px">
    <svg class="benefit-icon" viewBox="0 0 16 16" fill="none" stroke="#555" stroke-width=".8"><circle cx="8" cy="5" r="3.5" stroke="#e0141f"/><path d="M8 3v2h1.5" stroke="#e0141f"/><path d="M1 9l3 4h3M15 9l-3 4H9"/></svg>
    <div class="benefit-name">Finished in one weekend</div>
    <div class="benefit-text">Complete kits with clear step-by-step guides, so you can park on it by Monday.</div>
  </div>

  <div class="abs how"></div>
  <h2 class="abs section-title" style="top:359px;color:var(--white)">HOW IT WORKS</h2>
  <p class="abs how-text" style="top:378px">Pick your coating and colour, enter your garage's square footage and our configurator shows your exact price in real time.<br>We ship a complete kit with everything you need, from floor prep to topcoat, right to your driveway.</p>
  <div class="abs video" role="img" aria-label="Video still of an industrial coatings plant at sunset"></div>
  <svg class="abs play" viewBox="0 0 24 24"><circle cx="12" cy="12" r="12" fill="#e0141f"/><path d="M9.5 7.5v9l7-4.5z" fill="#fff"/></svg>

  <h2 class="abs section-title" style="top:592px">CLIENT <span class="red">REVIEWS</span></h2>
  <div class="abs review" style="left:35px;top:629px">
    <div class="stars">★★★★★</div>
    <p class="review-text">I was quoted over four thousand dollars by a local installer. I did the whole two-car garage myself in a weekend for a fraction of that, and it still looks like a showroom floor a year later.</p>
    <div class="reviewer"><div class="avatar" role="img" aria-label="Reviewer portrait"></div><div><div class="reviewer-name">John Doe</div><div class="reviewer-role">UAS</div></div></div>
  </div>
  <div class="abs review" style="left:197px;top:629px">
    <div class="stars">★★★★★</div>
    <p class="review-text">The configurator gave me an exact price before I ordered, and the kit had everything down to the rollers. Hot tires, oil drips and dropped tools haven't left a single mark on it.</p>
    <div class="reviewer"><div class="avatar" role="img" aria-label="Reviewer portrait"></div><div><div class="reviewer-name">John Doe</div><div class="reviewer-role">UAS</div></div></div>
  </div>

  <div class="abs card" style="left:37px;top:725px">
    <div class="card-photo card-photo--lift" role="img" aria-label="Workshop with blue car lifts on a glossy epoxy floor"></div>
    <div class="card-title">METALLIC EPOXY COATING</div>
    <p class="card-text">A deep, glossy metallic finish that stands up to car lifts, jacks and heavy tool chests.</p>
  </div>
  <div class="abs card" style="left:140px;top:725px">
    <div class="card-photo card-photo--lounge" role="img" aria-label="Bright living room with a polished epoxy floor"></div>
    <div class="card-title">METALLIC EPOXY COATING</div>
    <p class="card-text">Seamless and easy to clean, perfect for basements, home gyms and living spaces.</p>
  </div>
  <div class="abs card" style="left:243px;top:725px">
    <div class="card-photo card-photo--hall" role="img" aria-label="Long glossy corridor floor in a parking garage"></div>
    <div class="card-title">METALLIC EPOXY COATING</div>
    <p class="card-text">Chemical and abrasion resistant for high-traffic garages, shops and driveways.</p>
  </div>

  <div class="abs about-photo" role="img" aria-label="Large empty warehouse with a reflective epoxy floor"></div>
  <div class="abs about-label">ABOUT</div>
  <h2 class="abs about-title">RIDGELINE <span class="red">COATINGS</span></h2>
  <p class="abs about-text">We are the exclusive distributor of a US manufacturer of industrial-grade floor epoxies. For years these coatings were sold only to contractors and professional installers. Now we bring that same quality directly to homeowners, with kits, guides and real-time pricing made for DIY.</p>

  <footer class="abs footer">
    <div class="brand" style="left:35px;top:25px"><span class="brand-dot"></span>RIDGELINE COATINGS</div>
    <p class="abs copyright">© Copyright 2020 Ridgeline Coatings. All Rights Reserved</p>
  </footer>
</section>

</body>
</html>
```